Copper Kettle Auctions business card design with existing logo

Looking for a sleek and sexy design using our current logo

Contact Information for Business Card

Name, address, email, phone, website. Marcus Delvane 482 Brambleton Road Suite 210C Holtsville NY 11907 Copperkettlebids.net (631)555-0174

```html
<!DOCTYPE html>
<html lang="en">
<head>
<meta charset="utf-8">
<title>Copper Kettle Auctions – Business Card</title>
<link href="https://fonts.googleapis.com/css2?family=Arimo:wght@400&family=Michroma&display=swap" rel="stylesheet">
<style>
  :root {
    --bg: #2a2a2c;
    --card-dark: #1b1b1c;
    --card-light: #ffffff;
    --red: #d21f2b;
    --blue: #1d3f8a;
    --emboss: #6a6a6d;
    --rule: #d6d6d6;
  }
  * { margin: 0; padding: 0; box-sizing: border-box; }
  html, body { width: 1200px; height: 900px; overflow: hidden; }
  body {
    background: var(--bg);
    display: flex;
    flex-direction: column;
    align-items: center;
    justify-content: center;
    gap: 44px;
  }
  .card {
    width: 700px;
    height: 400px;
    position: relative;
  }
  .card--back {
    background: var(--card-dark);
    border-bottom: 4px solid var(--red);
    border-left: 2px solid var(--red);
    display: flex;
    align-items: center;
    justify-content: center;
  }
  .card--front {
    background: var(--card-light);
    border-bottom: 4px solid var(--blue);
    border-left: 2px solid var(--blue);
    display: flex;
    align-items: center;
  }
  .brand {
    display: flex;
    flex-direction: column;
    align-items: center;
    gap: 18px;
    font-family: "Michroma", sans-serif;
    text-align: center;
    text-transform: uppercase;
    letter-spacing: 1px;
    line-height: 1.15;
  }
  .brand__mark {
    width: 96px; height: 96px; border-radius: 50%;
    flex: none;
  }
  .brand__name { font-size: 36px; }
  .card--back .brand { color: var(--emboss); }
  .card--back .brand__mark { background: var(--emboss); }
  .card--back .brand__name { font-size: 40px; }
  .card--front .brand { color: var(--red); }
  .card--front .brand__mark { background: var(--blue); width: 84px; height: 84px; }
  .card--front .brand__name { font-size: 32px; }
  .front__logo {
    width: 52%;
    display: flex;
    justify-content: center;
    padding: 30px 10px 0 20px;
  }
  .front__divider {
    width: 1px;
    height: 250px;
    background: var(--rule);
  }
  .contact {
    padding-left: 34px;
    font-family: "Arimo", sans-serif;
    color: var(--blue);
    font-size: 16px;
  }
  .contact__name {
    font-family: "Michroma", sans-serif;
    color: var(--red);
    font-size: 15px;
    letter-spacing: 4px;
    text-transform: uppercase;
    margin-bottom: 16px;
  }
  .contact__line {
    display: flex;
    align-items: center;
    gap: 8px;
    margin-bottom: 6px;
  }
  .contact__line svg { width: 15px; height: 15px; flex: none; }
  .contact__web { color: var(--red); }
  .contact__address { margin-top: 16px; line-height: 1.35; }
</style>
</head>
<body>
  <section class="card card--back">
    <div class="brand">
      <span class="brand__mark"></span>
      <span class="brand__name">Copper Kettle<br>Auctions</span>
    </div>
  </section>

  <section class="card card--front">
    <div class="front__logo">
      <div class="brand">
        <span class="brand__mark"></span>
        <span class="brand__name">Copper Kettle<br>Auctions</span>
      </div>
    </div>
    <div class="front__divider"></div>
    <div class="contact">
      <p class="contact__name">Marcus Delvane</p>
      <p class="contact__line">
        <svg viewBox="0 0 24 24" fill="var(--red)"><path d="M6.6 10.8a15 15 0 0 0 6.6 6.6l2.2-2.2a1 1 0 0 1 1-.25 11.4 11.4 0 0 0 3.6.6 1 1 0 0 1 1 1V20a1 1 0 0 1-1 1A17 17 0 0 1 3 4a1 1 0 0 1 1-1h3.5a1 1 0 0 1 1 1c0 1.25.2 2.45.6 3.6a1 1 0 0 1-.25 1z"/></svg>
        (631)555-0174
      </p>
      <p class="contact__line">
        <svg viewBox="0 0 24 24" fill="var(--red)"><path d="M2 5h20v14H2z M2 5l10 8 10-8" stroke="#fff" stroke-width="1.5"/></svg>
        info@Copperkettlebids.net
      </p>
      <p class="contact__line">
        <svg viewBox="0 0 24 24" fill="none" stroke="var(--red)" stroke-width="2"><circle cx="12" cy="12" r="9"/><path d="M3 12h18M12 3c3 3 3 15 0 18M12 3c-3 3-3 15 0 18"/></svg>
        <span>www.<span class="contact__web">Copperkettlebids</span>.net</span>
      </p>
      <p class="contact__address">482 Brambleton Road Suite<br>210C Holtsville NY 11907</p>
    </div>
  </section>
</body>
</html>
```